Digital Marketing Consultant Needs a Business Card Design

I need a business card to brand myself - I'm a digital marketing consultant, and I do web design, SEO, lead generation, social media, etc. I'm overhauling my website (CorinneHalvorsk.com) and just had a snazzy new logo made.

I like the combo of yellow & gray - I find it eye-catching, upbeat and techie. The exact colors of yellow and gray that I like are #F6BF27 and #6D6D6D. But I'm open to suggestions and other color combinations!

I plan on printing the card using some high-end printing techniques that will ensure the card stands out - either really thick cards with colored edges, or spot UV. Not sure which yet, so if you want to incorporate that into your design, that'd be great!

I'm looking for a clean and modern design, but something that will really stand out when paired with 'fancy' printing.

Target Market(s)

Small and medium-sized business owners.

Industry/Entity Type

Printing

Contact Information for Business Card

Corinne Halvorsk
Digital Marketing
Call or Text: 850-555-0927
Corinne@CorinneHalvorsk.com
www.CorinneHalvorsk.com
@QPZ47 on Twitter

Font styles to use
Serif
Sans Serif

Requirements
Must have
• My logo, my contact information, and my "company colors" - #F6BF27 and #6D6D6D.
Nice to have
• If there's room to mention all the things that I do:
• Social Media, Web Design, SEO, Lead Generation, Conversion Funnels, PPC
• (don't add if it makes the card cluttered)

```html
<!DOCTYPE html>
<html lang="en">
<head>
<meta charset="utf-8">
<title>Corinne Halvorsk – Business Card</title>
<link rel="stylesheet" href="https://fonts.googleapis.com/css2?family=Marcellus&family=Montserrat:wght@400;500&display=swap">
<style>
  :root {
    --yellow: #F6BF27;
    --yellow-soft: #EFC85A;
    --gray: #6D6D6D;
    --gray-light: #9A9A9A;
    --rule: #B8B8B8;
    --paper: #FFFFFF;
    --backdrop: #E6E6E6;
    --serif: "Marcellus", "Times New Roman", serif;
    --sans: "Montserrat", Arial, sans-serif;
  }
  html, body {
    margin: 0;
    padding: 0;
    overflow: hidden;
  }
  .canvas {
    width: 1200px;
    height: 900px;
    background: var(--backdrop);
    display: flex;
    flex-direction: column;
    align-items: center;
    justify-content: center;
    gap: 56px;
  }
  .card {
    position: relative;
    width: 640px;
    height: 366px;
    background: var(--paper);
    border: 3px solid var(--yellow);
    box-sizing: border-box;
    box-shadow: 0 6px 18px rgba(0,0,0,0.12);
  }

  /* Contact side */
  .wordmark {
    position: absolute;
    left: 44px;
    top: 62px;
    margin: 0;
    font-family: var(--serif);
    font-weight: 400;
    font-size: 50px;
    letter-spacing: 3px;
    color: var(--gray-light);
    line-height: 1;
  }
  .tagline {
    position: absolute;
    right: 56px;
    top: 128px;
    margin: 0;
    font-family: var(--sans);
    font-size: 13px;
    letter-spacing: 4px;
    color: var(--gray);
  }
  .divider {
    position: absolute;
    left: 44px;
    right: 44px;
    top: 162px;
    height: 1px;
    background: var(--rule);
  }
  .contact {
    position: absolute;
    left: 56px;
    top: 184px;
    font-family: var(--sans);
    font-size: 13px;
    color: var(--gray);
    line-height: 1.55;
  }
  .contact .person { color: var(--yellow); font-weight: 500; }
  .contact .role { margin-bottom: 4px; }
  .contact ul { list-style: none; margin: 0; padding: 0; }
  .contact li { display: flex; align-items: center; gap: 8px; }
  .contact svg { width: 12px; height: 12px; flex: none; }

  /* Services side */
  .services {
    position: absolute;
    left: 400px;
    top: 70px;
    margin: 0;
    padding: 0;
    list-style: none;
    font-family: var(--sans);
    font-size: 14px;
    line-height: 1.35;
    color: var(--gray);
  }
  .services .accent { color: var(--yellow-soft); }
  .brand {
    position: absolute;
    left: 400px;
    top: 214px;
    display: flex;
    align-items: center;
    gap: 10px;
  }
  .brand-square {
    width: 30px;
    height: 30px;
    border: 3px solid var(--gray-light);
    box-sizing: border-box;
  }
  .brand-name {
    font-family: var(--serif);
    font-size: 18px;
    color: var(--gray-light);
    letter-spacing: 1px;
  }
</style>
</head>
<body>
<main class="canvas">

  <section class="card card-contact" aria-label="Contact side">
    <h1 class="wordmark">CORINNE HALVORSK</h1>
    <p class="tagline">digital marketing</p>
    <div class="divider"></div>
    <div class="contact">
      <div class="person">Corinne Halvorsk</div>
      <div class="role">founder &amp; owner</div>
      <ul>
        <li>
          <svg viewBox="0 0 12 12" aria-hidden="true"><circle cx="6" cy="6" r="6" fill="var(--yellow)"/><path d="M4 3.2 5 4.5 4.5 5.3Q5.4 6.8 6.7 7.5L7.5 7 8.8 8 8 9Q5.5 8.8 3.2 4Z" fill="#fff"/></svg>
          850-555-0927
        </li>
        <li>
          <svg viewBox="0 0 12 12" aria-hidden="true"><circle cx="6" cy="6" r="6" fill="var(--yellow)"/><rect x="3" y="4" width="6" height="4.2" fill="#fff"/><path d="M3 4 6 6.4 9 4" fill="none" stroke="var(--yellow)" stroke-width="0.7"/></svg>
          Corinne@CorinneHalvorsk.com
        </li>
        <li>
          <svg viewBox="0 0 12 12" aria-hidden="true"><circle cx="6" cy="6" r="6" fill="var(--yellow)"/></svg>
          @QPZ47
        </li>
        <li>
          <svg viewBox="0 0 12 12" aria-hidden="true"><circle cx="6" cy="6" r="6" fill="var(--yellow)"/><circle cx="6" cy="6" r="3" fill="none" stroke="#fff" stroke-width="0.8"/><path d="M3 6H9M6 3V9" stroke="#fff" stroke-width="0.6"/></svg>
          www.CorinneHalvorsk.com
        </li>
      </ul>
    </div>
  </section>

  <section class="card card-services" aria-label="Services side">
    <ul class="services">
      <li>Social Media</li>
      <li class="accent">Web Design</li>
      <li>SEO</li>
      <li class="accent">Lead Generation</li>
      <li>Conversion Funnels</li>
      <li class="accent">PPC</li>
    </ul>
    <div class="brand">
      <span class="brand-square" aria-hidden="true"></span>
      <span class="brand-name">Corinne Halvorsk</span>
    </div>
  </section>

</main>
</body>
</html>
```